Business card update

Opening a subsidiary of my company in the USA and need to update my logo.
Updates

Reason: Give more time to a good design.

I made a mistake on my briefing. It's only the business card. Thanks for alerting me on the mistake.

All the best

Leopoldo

Target Market(s)

We are an Executive Search company and our target audience are executives in large corporations.

Industry/Entity Type

Business

Requirements
Must have
• Keep the logo. In the US the company is called Declan Harrow Executive Search.

```html
<!DOCTYPE html>
<html lang="en">
<head>
<meta charset="utf-8">
<title>Declan Harrow Executive Search – Business Card</title>
<link rel="stylesheet" href="https://fonts.googleapis.com/css2?family=Josefin+Sans:wght@300;400&display=swap">
<style>
  :root {
    --page-bg: #2a2a2a;
    --teal-deep: #1f9aa8;
    --teal-mid: #34aebb;
    --teal-light: #55c3cf;
    --ink-white: #ffffff;
  }
  * { box-sizing: border-box; margin: 0; padding: 0; }
  html, body {
    width: 1200px;
    height: 852px;
    overflow: hidden;
    background: var(--page-bg);
  }
  .canvas {
    position: relative;
    width: 1200px;
    height: 852px;
  }
  .business-card {
    position: absolute;
    left: 50px;
    top: 105px;
    width: 1100px;
    height: 642px;
    overflow: hidden;
    background: radial-gradient(ellipse at 72% 60%, var(--teal-light) 0%, var(--teal-mid) 50%, var(--teal-deep) 100%);
    font-family: "Josefin Sans", "Futura", sans-serif;
    font-weight: 300;
    color: var(--ink-white);
  }
  .brand-name {
    position: absolute;
    left: 56px;
    top: 190px;
    font-size: 46px;
    line-height: 1.15;
    font-weight: 400;
    color: var(--ink-white);
  }
  .brand-name span { display: block; }
  .holder-name {
    position: absolute;
    right: 69px;
    top: 128px;
    font-size: 41px;
    font-weight: 300;
    letter-spacing: 0.5px;
    text-transform: uppercase;
    text-align: right;
    white-space: nowrap;
  }
  .contact-list {
    position: absolute;
    right: 69px;
    top: 332px;
    list-style: none;
    text-align: right;
    font-size: 41px;
    line-height: 43.5px;
    white-space: nowrap;
  }
</style>
</head>
<body>
<main class="canvas">
  <article class="business-card">
    <div class="brand-name">
      <span>Declan</span>
      <span>Harrow</span>
      <span>Executive Search</span>
    </div>

    <h1 class="holder-name">Leopoldo D. Harrow</h1>

    <ul class="contact-list">
      <li class="contact-street">4810 Harborview Ave Suite 200</li>
      <li class="contact-city">Bayside FL 33190</li>
      <li class="contact-phone">555 014-0187</li>
      <li class="contact-web">www.dhexecutivesearch.com</li>
      <li class="contact-email">lharrow@dhexecutivesearch.com</li>
    </ul>
  </article>
</main>
</body>
</html>
```